Quillfern Rise A4 Potrait foldout brochure

We need a brochure design for this residential land development. I have attached the a style that we like to base our design on. Full colour required. will provide files required for design also. PLEASE DO NOT COPY THIS DESIGN. Come up with a new style that gives you this feeling. Please note the plan needs to be positioned landscape on the inside 2 A4 Pages.

Industry/Entity Type

Residential

Font styles to use
Other font styles liked:
• Try with Century Gothich

Requirements
Must have
• use same colours as supplied in Quillfern rise brochure.
Nice to have
• nice modern simple background graphics

```html
<!DOCTYPE html>
<html lang="en">
<head>
<meta charset="utf-8">
<title>Quillfern Rise – Brochure Covers</title>
<link href="https://fonts.googleapis.com/css2?family=Questrial&family=Lato:wght@400;700&display=swap" rel="stylesheet">
<style>
  :root {
    --paper: #ffffff;
    --backdrop: #e9eaec;
    --green-dark: #1c5a27;
    --green-light: #6cb33f;
    --rule: #d6d8d6;
    --fold: #dcdcdc;
    --sage: #9fb7b0;
    --sky: #8fc3df;
    --navy: #5e6f9a;
    --rose: #e8909f;
    --peach: #f3b48f;
    --lime: #e9ea78;
    --leaf: #8ec07c;
  }
  * { box-sizing: border-box; margin: 0; padding: 0; }
  html, body { width: 1200px; height: 867px; overflow: hidden; background: var(--backdrop); }
  .spread { position: relative; width: 1200px; height: 867px; display: flex; }
  .page { position: relative; width: 600px; height: 867px; background: var(--paper); overflow: hidden; }
  .page--back { border-right: 1px solid var(--fold); }
  .pattern { position: absolute; inset: 0; width: 600px; height: 867px; }

  .contact-panel {
    position: absolute; left: 127px; top: 476px; width: 332px; height: 365px;
    background: rgba(255,255,255,0.82); border-radius: 6px;
    text-align: center; font-family: "Lato", sans-serif; color: var(--green-dark);
  }
  .contact-panel .brand-name {
    position: absolute; top: 140px; left: 0; right: 0;
    font-family: "Questrial", sans-serif; font-size: 31px; font-weight: 400; color: var(--green-dark);
  }
  .contact-panel .rule { position: absolute; top: 185px; left: 8px; right: 8px; height: 1px; background: var(--rule); }
  .contact-list { position: absolute; top: 198px; left: 0; right: 0; list-style: none; }
  .contact-list li { display: flex; justify-content: center; align-items: flex-start; gap: 6px; font-size: 16px; line-height: 20px; }
  .contact-list .address { margin-bottom: 6px; }
  .contact-list .address span { text-align: center; }
  .contact-list .phone { font-size: 19px; font-weight: 700; margin-bottom: 6px; align-items: center; }
  .contact-list .email, .contact-list .web { font-size: 15px; margin-bottom: 4px; align-items: center; }
  .icon { flex: none; fill: var(--green-light); }

  .cover-title {
    position: absolute; top: 280px; left: 68px; width: 460px;
    font-family: "Questrial", sans-serif; font-size: 58px; font-weight: 400;
    color: var(--green-dark); letter-spacing: -0.5px; white-space: nowrap;
  }
  .cover-web {
    position: absolute; left: 128px; top: 781px; width: 332px; height: 58px;
    background: rgba(255,255,255,0.85); border-radius: 6px;
    font-family: "Lato", sans-serif; font-size: 24px; text-align: center; line-height: 52px;
    color: var(--green-dark);
  }
  .cover-web .accent { color: var(--green-light); }
  .cover-web::after { content: ""; position: absolute; left: 10px; right: 10px; bottom: 10px; height: 1px; background: var(--rule); }
</style>
</head>
<body>
<main class="spread">

  <section class="page page--back">
    <svg class="pattern" viewBox="0 0 600 867" role="img" aria-label="Soft pastel backdrop of overlapping rounded square outlines">
      <defs>
        <linearGradient id="backTop" x1="0" y1="0" x2="1" y2="1">
          <stop offset="0" stop-color="var(--sage)" stop-opacity="0.45"/>
          <stop offset="0.5" stop-color="var(--sky)" stop-opacity="0.4"/>
          <stop offset="1" stop-color="var(--navy)" stop-opacity="0.5"/>
        </linearGradient>
        <linearGradient id="backLow" x1="0" y1="0" x2="1" y2="1">
          <stop offset="0" stop-color="var(--navy)" stop-opacity="0.35"/>
          <stop offset="0.35" stop-color="var(--rose)" stop-opacity="0.4"/>
          <stop offset="0.65" stop-color="var(--peach)" stop-opacity="0.35"/>
          <stop offset="1" stop-color="var(--lime)" stop-opacity="0.45"/>
        </linearGradient>
      </defs>
      <path d="M310 40 L600 0 L600 680 L470 560 Q390 420 300 200 Z" fill="url(#backTop)"/>
      <path d="M140 430 Q300 330 600 280 L600 867 L420 867 Q250 700 140 430 Z" fill="url(#backLow)"/>
    </svg>

    <div class="contact-panel">
      <h2 class="brand-name">Quillfern Rise</h2>
      <div class="rule"></div>
      <ul class="contact-list">
        <li class="address">
          <svg class="icon" width="11" height="15" viewBox="0 0 12 16"><path d="M6 0a6 6 0 0 0-6 6c0 4.5 6 10 6 10s6-5.5 6-10a6 6 0 0 0-6-6zm0 8.5A2.5 2.5 0 1 1 6 3.5a2.5 2.5 0 0 1 0 5z"/></svg>
          <span>Quillfern Rise<br>Larkspur Lane 42b<br>20817 City, State</span>
        </li>
        <li class="phone">
          <svg class="icon" width="18" height="18" viewBox="0 0 20 20"><circle cx="10" cy="10" r="9" fill="none" stroke="var(--green-light)" stroke-width="1.6"/><path d="M7 5.5l1.6 2.4-1 1.1c.6 1.3 1.6 2.3 2.9 2.9l1.1-1 2.4 1.6-.8 1.8c-3.6-.2-6.9-3.5-7.1-7.1z"/></svg>
          <span>+01 98 7654321</span>
        </li>
        <li class="email">
          <svg class="icon" width="16" height="12" viewBox="0 0 16 12"><path d="M0 0h16v12H0z"/><path d="M0 0l8 6 8-6" fill="none" stroke="#fff" stroke-width="1.4"/></svg>
          <span>info@quillfernrise.com</span>
        </li>
        <li class="web">
          <svg class="icon" width="15" height="15" viewBox="0 0 16 16"><g fill="none" stroke="var(--green-light)" stroke-width="1.3"><circle cx="8" cy="8" r="7"/><ellipse cx="8" cy="8" rx="3" ry="7"/><path d="M1 8h14M2.5 4.5h11M2.5 11.5h11"/></g></svg>
          <span>www.quillfernrise.com</span>
        </li>
      </ul>
    </div>
  </section>

  <section class="page page--cover">
    <svg class="pattern" viewBox="0 0 600 867" role="img" aria-label="Soft pastel backdrop of overlapping rounded square outlines">
      <defs>
        <linearGradient id="coverTop" x1="0" y1="0" x2="1" y2="1">
          <stop offset="0" stop-color="var(--sage)" stop-opacity="0.45"/>
          <stop offset="0.5" stop-color="var(--sky)" stop-opacity="0.4"/>
          <stop offset="1" stop-color="var(--navy)" stop-opacity="0.5"/>
        </linearGradient>
        <linearGradient id="coverLow" x1="0" y1="0" x2="1" y2="1">
          <stop offset="0" stop-color="var(--navy)" stop-opacity="0.4"/>
          <stop offset="0.3" stop-color="var(--rose)" stop-opacity="0.45"/>
          <stop offset="0.55" stop-color="var(--sky)" stop-opacity="0.4"/>
          <stop offset="0.8" stop-color="var(--leaf)" stop-opacity="0.4"/>
          <stop offset="1" stop-color="var(--lime)" stop-opacity="0.5"/>
        </linearGradient>
      </defs>
      <path d="M300 30 L600 0 L600 600 L470 520 Q400 330 320 220 Z" fill="url(#coverTop)"/>
      <path d="M140 400 Q340 330 600 240 L600 867 L200 867 Q150 640 140 400 Z" fill="url(#coverLow)"/>
    </svg>

    <h1 class="cover-title">Quillfern Rise</h1>

    <p class="cover-web"><span class="accent">www.</span>quillfernrise<span class="accent">.com</span></p>
  </section>

</main>
</body>
</html>
```